Occupational Therapy Needs an eye catching brochure for new business

I need a brochure for a new business that would be eye catching. I am an occupational therapist and this business will specifically deal with auditory processing delays and visual processing delays.If the childs delays stem from unintegrated reflexes that will be dealt with,as well. I have attached a brochure that I created. After having created it I decided that I wanted to seek professional graphics artist to help create an eye catching brochure that would attract more attention then my current unprofessional one. The attached brochures backgrounds should be changed. The wording should be changed and be more professionalized but the message should stay. I do not have a logo, since I am new, so you can create one for me, as well.
Updates

Please keep it a tri-fold. I have added the original brother file .edit and a word document with my text inside. Please give the brochure a professional look. I want those seeing my brochure to get the feel that my therapy business is a very professional and experienced business.Thank You Added Sunday, April 26, 2015

Target Market(s)

Parents of children with learning delays, whom are struggling and not getting good grades in school.

Industry/Entity Type

Business

Requirements
Must have
• Please keep it a tri-fold brochure
Nice to have
• Please include on the front page the following questions, they can be worded differently:
• Does your child have difficulty learning ABC and /or aleph bet?
• Does your child know the information for the test and does not do well on the test?
• Does your child have difficulty remembering name and dates in school, for test, or every day life?
Should not have
• Please do not include pictures of Adults in the brochure.

```html
<!DOCTYPE html>
<html lang="en">
<head>
<meta charset="utf-8">
<title>How It Unfolds – Tri-fold Brochure</title>
<link href="https://fonts.googleapis.com/css2?family=Jost:wght@300;400;500;600;800&display=swap" rel="stylesheet">
<style>
  :root {
    --ink: #1a1a1a;
    --paper: #ffffff;
    --green: #8cc63f;
    --lime: #c8d92b;
    --yellow: #ffd21f;
    --amber: #f7a823;
    --orange: #f26a21;
    --blue: #2aa8e0;
    --sky: #5cb8e6;
    --pink: #e6197d;
    --brand: #6cb33f;
    --teal: #2f8f9d;
    --violet: #6b4c9a;
  }
  * { box-sizing: border-box; margin: 0; padding: 0; }
  html, body { width: 1200px; height: 2388px; overflow: hidden; background: var(--paper); }
  body { position: relative; font-family: "Jost", sans-serif; color: var(--ink); }

  .board-title {
    position: absolute; left: 136px; top: 92px;
    font-size: 64px; font-weight: 800; letter-spacing: 1px; line-height: 1;
  }
  .stage-label {
    position: absolute; font-size: 44px; font-weight: 300; letter-spacing: 1px; line-height: 1;
  }

  .sheet { position: absolute; border: 2px solid var(--ink); background: var(--paper); }
  .panel {
    position: absolute; border-radius: 14px; color: var(--paper); text-align: center;
    padding: 0 12px;
  }
  .panel-heading {
    font-weight: 400; text-transform: uppercase; line-height: 1.02; letter-spacing: 0.5px;
  }
  .panel-copy { font-size: 9px; line-height: 1.45; font-weight: 400; margin-top: 12px; }
  .panel-copy strong { font-weight: 600; }
  .icon-ring {
    width: 30px; height: 30px; margin: 0 auto 10px; border: 2px solid var(--paper);
    border-radius: 50%; display: flex; align-items: center; justify-content: center;
  }
  .brand-name {
    position: absolute; font-family: "Jost", sans-serif; font-weight: 500; color: var(--brand);
    font-size: 11px; line-height: 1; text-align: right;
  }

  /* Front */
  .front { left: 386px; top: 330px; width: 196px; height: 410px; }
  .front-art {
    position: absolute; left: 10px; top: 14px; width: 176px; height: 346px; border-radius: 14px;
    background:
      radial-gradient(ellipse 60% 40% at 30% 20%, rgba(247,168,35,.85), transparent 70%),
      radial-gradient(ellipse 50% 45% at 80% 35%, rgba(140,198,63,.8), transparent 70%),
      radial-gradient(ellipse 55% 40% at 50% 85%, rgba(242,106,33,.85), transparent 70%),
      linear-gradient(160deg, var(--teal) 0%, var(--violet) 45%, var(--green) 75%, var(--amber) 100%);
  }
  .front-text { position: absolute; left: 10px; top: 52px; width: 176px; }
  .front-text .panel-heading { font-size: 33px; line-height: 0.98; }
  .front-text .panel-copy { font-size: 8.5px; padding: 0 14px; }

  /* First opening */
  .opening-svg { position: absolute; left: 230px; top: 800px; }
  .opening-right { left: 386px; top: 840px; width: 170px; height: 426px; }

  /* Inside spread */
  .spread { left: 210px; top: 1428px; width: 560px; height: 402px; }
  .fold-line { position: absolute; top: 0; width: 2px; height: 100%; background: var(--ink); }
  .panel-auditory { left: 16px; top: 28px; width: 146px; height: 320px; background: linear-gradient(180deg, var(--green) 0%, var(--lime) 45%, var(--amber) 100%); }
  .panel-visual { left: 188px; top: 28px; width: 150px; height: 350px; background: linear-gradient(180deg, var(--blue) 0%, #6cc5d8 55%, #d9e87a 100%); }
  .panel-combined { left: 364px; top: 28px; width: 180px; height: 320px; background: linear-gradient(180deg, var(--pink) 0%, var(--orange) 45%, var(--yellow) 100%); }
  .spread .panel { padding-top: 16px; }
  .spread .panel-heading { font-size: 17px; }

  /* Back */
  .back { left: 386px; top: 1914px; width: 168px; height: 346px; }
  .back-heading { position: absolute; left: 10px; top: 86px; width: 146px; }
  .back-heading .panel-heading { font-size: 22px; }
  .back-heading .panel-copy { font-size: 7.5px; margin-top: 6px; }
  .back-contact { position: absolute; left: 10px; top: 246px; width: 146px; }
  .back-contact .panel-copy { font-size: 7.5px; margin-top: 0; }
</style>
</head>
<body>

  <h1 class="board-title">HOW IT UNFOLDS</h1>

  <!-- Front cover -->
  <div class="stage-label" style="left:624px; top:338px;">FRONT</div>
  <div class="sheet front">
    <div class="front-art" role="img" aria-label="Abstract flowing shapes in teal, violet, green, yellow and orange with a fine dot texture"></div>
    <div class="front-text panel">
      <div class="panel-heading">Help your child flourish</div>
      <p class="panel-copy">Does your child find it hard to learn letters?<br><br>Does your child know the material but test poorly?<br><br>Is remembering names and dates a daily struggle?</p>
    </div>
    <div class="brand-name" style="right:10px; bottom:14px;">Bright Steps<br>OT services</div>
  </div>

  <!-- First opening -->
  <div class="stage-label" style="left:810px; top:870px;">FIRST OPENING</div>
  <svg class="opening-svg" width="160" height="480" viewBox="0 0 160 480" aria-hidden="true">
    <defs>
      <linearGradient id="audGrad" x1="0" y1="0" x2="0" y2="1">
        <stop offset="0" stop-color="#8cc63f"/>
        <stop offset="0.45" stop-color="#c8d92b"/>
        <stop offset="1" stop-color="#f7a823"/>
      </linearGradient>
    </defs>
    <polygon points="10,10 156,40 156,466 14,440" fill="#fff" stroke="#1a1a1a" stroke-width="2"/>
    <path d="M34,32 L136,52 Q146,54 146,64 L146,420 Q146,430 136,428 L36,412 Q26,410 26,400 L26,42 Q26,30 34,32 Z" fill="url(#audGrad)"/>
    <g transform="matrix(0.9,0.2,0,1,0,0)" fill="#fff" font-family="Jost, sans-serif" text-anchor="middle">
      <circle cx="95" cy="80" r="14" fill="none" stroke="#fff" stroke-width="2"/>
      <text x="95" y="122" font-size="15">AUDITORY</text>
      <text x="95" y="140" font-size="15">PROCESSING</text>
      <text x="95" y="172" font-size="7.5">Some children hear well but</text>
      <text x="95" y="184" font-size="7.5">find spoken information hard</text>
      <text x="95" y="196" font-size="7.5">to hold and use.</text>
    </g>
  </svg>
  <div class="sheet opening-right">
    <svg width="166" height="422" viewBox="0 0 166 422" style="position:absolute; left:0; top:0;" aria-hidden="true">
      <defs>
        <linearGradient id="benefitGrad" x1="0" y1="0" x2="0" y2="1">
          <stop offset="0" stop-color="#ffd21f"/>
          <stop offset="0.5" stop-color="#f7a823"/>
          <stop offset="1" stop-color="#f26a21"/>
        </linearGradient>
      </defs>
      <path d="M24,16 H144 Q156,16 156,28 V358 Q156,370 144,370 H58 Q46,370 42,358 Q36,338 12,334 V28 Q12,16 24,16 Z" fill="url(#benefitGrad)"/>
      <path d="M0,352 Q30,352 38,380 Q42,392 40,422" fill="none" stroke="#1a1a1a" stroke-width="2"/>
    </svg>
    <div class="panel" style="left:12px; top:34px; width:144px; padding:0 10px;">
      <div class="panel-heading" style="font-size:19px;">What is the benefit of having an <strong style="font-weight:600;">OT</strong> work on auditory processing skills?</div>
      <p class="panel-copy" style="font-size:8px;">Working on auditory processing helps a child follow lessons, recall instructions and join in with confidence.<br><br><strong>Only research based programs are used</strong></p>
    </div>
  </div>

  <!-- Inside spread -->
  <div class="stage-label" style="left:806px; top:1430px;">INSIDE SPREAD</div>
  <div class="sheet spread">
    <div class="fold-line" style="left:172px;"></div>
    <div class="fold-line" style="left:350px;"></div>

    <div class="panel panel-auditory">
      <div class="icon-ring"><svg width="14" height="16" viewBox="0 0 14 16" aria-hidden="true"><path d="M3,6 Q3,1 7,1 Q12,1 12,6 Q12,9 9,11 Q8,12 8,14 Q7,15 5,15" fill="none" stroke="#fff" stroke-width="1.6"/></svg></div>
      <div class="panel-heading">Auditory processing</div>
      <p class="panel-copy">Some children with auditory delays have <strong>difficulty processing and remembering information that they hear.</strong><br><br>This affects following directions, especially in the younger grades.</p>
    </div>

    <div class="panel panel-visual">
      <div class="icon-ring"><svg width="18" height="12" viewBox="0 0 18 12" aria-hidden="true"><path d="M1,6 Q9,-3 17,6 Q9,15 1,6 Z" fill="none" stroke="#fff" stroke-width="1.6"/><circle cx="9" cy="6" r="2.4" fill="#fff"/></svg></div>
      <div class="panel-heading">Visual processing</div>
      <p class="panel-copy">Children with visual delays have <strong>difficulty processing and remembering information that they see.</strong><br><br>They may reverse letters, lose their place or copy slowly from the board.</p>
    </div>

    <div class="panel panel-combined">
      <div class="panel-heading" style="margin-top:4px;">Combining visual and auditory information</div>
      <p class="panel-copy">Some children have <strong>difficulty combining what they hear with what they see.</strong><br><br>Targeted exercises build these links step by step.</p>
    </div>

    <div class="brand-name" style="right:14px; bottom:12px;">Bright Steps<br>OT services</div>
  </div>

  <!-- Back -->
  <div class="stage-label" style="left:624px; top:1918px;">BACK</div>
  <div class="sheet back">
    <svg width="164" height="342" viewBox="0 0 164 342" style="position:absolute; left:0; top:0;" aria-hidden="true">
      <defs>
        <linearGradient id="backGrad" x1="0" y1="0" x2="0" y2="1">
          <stop offset="0" stop-color="#5cb8e6"/>
          <stop offset="0.45" stop-color="#8ccdee"/>
          <stop offset="0.6" stop-color="#ffffff"/>
          <stop offset="0.74" stop-color="#8cc63f"/>
          <stop offset="1" stop-color="#6cb33f"/>
        </linearGradient>
      </defs>
      <path d="M48,16 H146 Q156,16 156,28 V290 Q156,302 144,302 H22 Q10,302 10,290 V66 Q34,62 40,40 Q42,16 48,16 Z" fill="url(#backGrad)"/>
      <path d="M0,50 Q26,50 32,26 Q34,10 30,0" fill="none" stroke="#1a1a1a" stroke-width="2"/>
    </svg>
    <div class="panel back-heading">
      <div class="panel-heading">Free evaluation</div>
      <p class="panel-copy">Book a free first session for your child.</p>
    </div>
    <div class="panel back-contact">
      <p class="panel-copy">Call 555-0142 to book today<br>Monday to Thursday</p>
    </div>
    <div class="brand-name" style="right:10px; bottom:8px; font-size:10px;">Bright Steps<br>OT services</div>
  </div>

</body>
</html>
```